Investment company needing business card

We are wanting a business card which looks sharp and easy on the eye. We are thinking of having a business card with the logo embossed on it, to really make it stand out. We will only have a small amount of information of the business card, person's name, position, email address and phone number

Contact Information for Business Card

Danica Pruett
Executive Assistant
+64 21 547 3162
danicap@harwellcapital.co.nz

Requirements
Must have
• Embossed logo
Should not have
• Not to be busy

```html
<!DOCTYPE html>
<html lang="en">
<head>
<meta charset="utf-8">
<title>Ashford Group – Business Card</title>
<link href="https://fonts.googleapis.com/css2?family=Roboto:wght@400;500;700&display=swap" rel="stylesheet">
<style>
  :root {
    --page: #1c1d1f;
    --card: #0d0d0e;
    --green: #3cc47c;
    --grey: #8e8f91;
    --light: #d6d6d6;
    --rule: #6b6c6e;
  }
  * { margin: 0; padding: 0; box-sizing: border-box; }
  html, body {
    width: 1200px;
    height: 900px;
    overflow: hidden;
    background: var(--page);
    font-family: "Roboto", Arial, sans-serif;
  }
  .stage {
    width: 1200px;
    height: 900px;
    display: flex;
    align-items: center;
    justify-content: center;
  }
  .card {
    position: relative;
    width: 980px;
    height: 560px;
    background: var(--card);
    box-shadow: 0 20px 50px rgba(0,0,0,.55);
    display: flex;
    align-items: center;
  }
  .brand {
    width: 500px;
    padding-left: 90px;
    display: flex;
    align-items: center;
    gap: 22px;
  }
  .brand-mark {
    width: 58px;
    height: 58px;
    background: var(--green);
    flex: none;
  }
  .brand-name {
    color: var(--green);
    font-weight: 700;
    font-size: 44px;
    letter-spacing: 2px;
    text-transform: uppercase;
    line-height: 1;
  }
  .divider {
    width: 3px;
    height: 210px;
    background: var(--rule);
    margin-right: 60px;
  }
  .person-name {
    color: var(--green);
    font-weight: 700;
    font-size: 46px;
    line-height: 1.05;
  }
  .person-role {
    display: inline-block;
    color: var(--grey);
    font-size: 20px;
    font-weight: 500;
    padding: 4px 14px 8px 4px;
    border-bottom: 2px solid var(--rule);
    margin-bottom: 26px;
  }
  .contact-list { list-style: none; }
  .contact-item {
    display: flex;
    align-items: center;
    gap: 16px;
    color: var(--light);
    font-size: 21px;
    font-weight: 500;
    margin-bottom: 12px;
  }
  .contact-icon { width: 22px; height: 22px; flex: none; }
</style>
</head>
<body>
  <main class="stage">
    <section class="card" aria-label="Business card">
      <div class="brand">
        <span class="brand-mark" aria-hidden="true"></span>
        <span class="brand-name">Ashford Group</span>
      </div>
      <div class="divider" aria-hidden="true"></div>
      <div class="details">
        <h1 class="person-name">Reuben Hale</h1>
        <p class="person-role">Company Director</p>
        <ul class="contact-list">
          <li class="contact-item">
            <svg class="contact-icon" viewBox="0 0 24 24" aria-hidden="true">
              <rect x="1" y="1" width="22" height="22" rx="3" fill="none" stroke="#3cc47c" stroke-width="2"/>
              <path d="M8 6c-1 1-1 3 1 6s4 5 6 5l1.5-1.5-2.2-2.2-1.3 1c-1-.6-2.4-2-3-3l1-1.3L8.8 6z" fill="#3cc47c"/>
            </svg>
            <span>0412 583 204</span>
          </li>
          <li class="contact-item">
            <svg class="contact-icon" viewBox="0 0 24 24" aria-hidden="true">
              <rect x="1" y="4" width="22" height="16" fill="none" stroke="#3cc47c" stroke-width="2"/>
              <path d="M1 4l11 9 11-9" fill="none" stroke="#3cc47c" stroke-width="2"/>
            </svg>
            <span>reuben@ashfordgroup.com</span>
          </li>
        </ul>
      </div>
    </section>
  </main>
</body>
</html>
```